Ecommerce website for custom sign, woodworking, and jewelry

Fully design an ecommerce website which can be loaded into my current website. Must be able to update and modify myself

```html
<!DOCTYPE html>
<html lang="en">
<head>
<meta charset="utf-8">
<title>Oakmere Creations, LLC</title>
<link href="https://fonts.googleapis.com/css2?family=Merriweather:wght@400;700&family=Lato:ital,wght@0,400;0,700;1,400&display=swap" rel="stylesheet">
<style>
:root{
  --brown:#6b3a22;
  --brown-band:#7d4b2f;
  --ink:#222;
  --text:#444;
  --muted:#777;
  --gold:#e0a800;
  --line:#e6e6e6;
  --footer:#3b3b3b;
  --footer-bar:#3a2a21;
  --white:#fff;
}
*{box-sizing:border-box;margin:0;padding:0}
html,body{width:1200px;height:3690px;overflow:hidden}
body{font-family:"Lato",sans-serif;color:var(--text);background:var(--white);position:relative}
.abs{position:absolute}
.serif{font-family:"Merriweather",serif}

/* header */
.logo{left:110px;top:28px;font-family:"Merriweather",serif;font-weight:700;font-size:26px;color:var(--brown)}
.search{left:447px;top:24px;width:296px;height:48px;border:1px solid #ddd;border-radius:24px;box-shadow:0 2px 6px rgba(0,0,0,.08)}
.search span{position:absolute;left:28px;top:15px;font-size:15px;color:#888}
.search .btn{position:absolute;right:5px;top:5px;width:38px;height:38px;border-radius:50%;background:var(--brown)}
.account{left:783px;top:40px;font-size:13px;color:#555;letter-spacing:.3px}
.account b{font-weight:400;margin:0 8px}
.cart{left:1046px;top:30px;width:36px;height:36px;border:2px solid var(--brown);border-radius:50%}
.cart .count{position:absolute;right:-8px;top:-8px;width:18px;height:18px;border-radius:50%;background:var(--brown);color:#fff;font-size:11px;text-align:center;line-height:18px}
.nav{left:113px;top:100px;display:flex;gap:34px;font-size:14px;font-weight:700;color:#222}
.nav .active{color:var(--brown);border-bottom:2px solid var(--brown);padding-bottom:4px}
.header-rule{left:0;top:129px;width:1200px;height:1px;background:var(--line)}

/* hero */
.hero{left:0;top:130px;width:1200px;height:557px;background:radial-gradient(ellipse at 55% 45%,#b78c60,#8a6440 55%,#4a3524)}
.hero h1{position:absolute;left:0;width:1200px;top:160px;text-align:center;font-family:"Merriweather",serif;font-weight:700;font-size:66px;line-height:74px;color:#fff;text-shadow:0 2px 6px rgba(0,0,0,.45)}
.btn-outline{position:absolute;height:50px;border:2px solid #fff;border-radius:3px;color:#fff;font-size:14px;font-weight:700;display:flex;align-items:center;justify-content:center;gap:10px;letter-spacing:.3px}
.hero .btn-outline{left:527px;top:340px;width:146px;background:rgba(60,35,20,.35)}
.dots{position:absolute;left:573px;top:491px;display:flex;gap:4px}
.dots i{width:9px;height:9px;border-radius:50%;background:#fff;border:1px solid #fff}
.dots i.off{background:transparent}

/* sections */
.section-title{left:0;width:1200px;text-align:center;font-family:"Merriweather",serif;font-weight:700;font-size:42px;color:var(--ink)}
.card{width:232px;height:318px;background:#fff;box-shadow:0 0 8px rgba(0,0,0,.12)}
.card .photo{position:absolute;left:3px;top:3px;width:226px;height:175px}
.card .name{position:absolute;top:214px;width:100%;text-align:center;font-size:14px;font-weight:700;color:#222}
.card .stars{position:absolute;top:240px;width:100%;text-align:center;color:var(--gold);font-size:15px;letter-spacing:2px}
.card .price{position:absolute;top:262px;width:100%;text-align:center;font-size:27px;color:#333}

.about{left:0;top:1277px;width:1200px;height:477px;background:linear-gradient(100deg,#3b2c20 0%,#5a4738 40%,#5d6670 70%,#9aa6b3 100%)}
.about h2{position:absolute;left:0;width:1200px;top:80px;text-align:center;font-family:"Merriweather",serif;font-weight:700;font-size:44px;color:#fff;text-shadow:0 2px 5px rgba(0,0,0,.4)}
.about p{position:absolute;left:240px;width:720px;top:162px;text-align:center;font-size:15px;line-height:30px;color:#fff}
.about .btn-outline{left:527px;top:338px;width:146px;background:rgba(0,0,0,.3)}

.testimonial{left:0;top:2316px;width:1200px;height:372px;background:linear-gradient(90deg,#7a492d,#845236 50%,#7a492d)}
.testimonial h2{position:absolute;left:380px;top:80px;font-family:"Merriweather",serif;font-weight:700;font-size:40px;color:#fff}
.arrow{position:absolute;top:47px;width:34px;height:33px;background:#fff;border-radius:3px}
.avatar{position:absolute;left:166px;top:158px;width:112px;height:112px;border-radius:50%;background:linear-gradient(#d9d4cf,#9c9894);border:3px solid #fff}
.vrule{position:absolute;left:328px;top:154px;width:1px;height:122px;background:rgba(255,255,255,.6)}
.quote-text{position:absolute;left:425px;top:154px;width:640px;font-style:italic;font-size:14px;line-height:26px;color:#fff}
.testimonial .btn-outline{left:425px;top:247px;width:148px;height:45px;font-size:14px}
.client{position:absolute;left:906px;top:250px;font-size:19px;color:#fff}

.post{width:317px;height:440px;background:#fff;box-shadow:0 0 8px rgba(0,0,0,.12)}
.post .photo{position:absolute;left:3px;top:3px;width:311px;height:219px}
.post h3{position:absolute;left:20px;top:252px;width:285px;font-size:14px;font-weight:700;line-height:26px;color:#222}
.post p{position:absolute;left:20px;top:308px;width:285px;font-size:14px;line-height:23px;color:#777}
.post .meta{position:absolute;left:0;top:382px;width:100%;border-top:1px solid var(--line);padding:24px 0 0 22px;font-size:14px;color:#777;display:flex;gap:28px;align-items:center}
.post .meta span{display:flex;align-items:center;gap:10px}

.footer{left:0;top:3408px;width:1200px;height:231px;background:var(--footer)}
.footer .brand{position:absolute;left:86px;top:100px;font-family:"Merriweather",serif;font-weight:700;font-size:26px;color:#fff}
.contact{position:absolute;left:389px;top:72px;display:flex;align-items:center;font-size:15px;color:#fff}
.contact span{display:flex;align-items:center;gap:14px}
.contact .sep{margin:0 36px;color:#ccc}
.frule{position:absolute;left:388px;top:115px;width:719px;height:1px;background:#777}
.fnav{position:absolute;left:388px;top:138px;display:flex;gap:34px;font-size:14px;font-weight:700;color:#fff}
.bottom-bar{left:0;top:3639px;width:1200px;height:51px;background:var(--footer-bar)}
.bottom-bar .copy{position:absolute;left:110px;top:17px;font-size:14px;color:#fff}
.pay{position:absolute;left:968px;top:10px;width:116px;height:30px;border:1px solid #888;border-radius:3px;display:flex;align-items:center;justify-content:center;gap:6px}
.pay i{width:22px;height:14px;border-radius:2px;background:#8a8a8a}
</style>
</head>
<body>

<header>
  <div class="abs logo">Oakmere Creations, LLC</div>
  <div class="abs search"><span>Search</span>
    <div class="btn"><svg width="38" height="38" viewBox="0 0 38 38"><circle cx="18" cy="18" r="5" fill="none" stroke="#fff" stroke-width="2"/><line x1="21.5" y1="21.5" x2="25" y2="25" stroke="#fff" stroke-width="2.4" stroke-linecap="round"/></svg></div>
  </div>
  <div class="abs account">LOGIN<b>/</b>REGISTER &nbsp;&nbsp;&nbsp; CHECKOUT</div>
  <div class="abs cart">
    <svg width="32" height="32" viewBox="0 0 32 32"><path d="M8 10h3l2 9h9l2-7H12" fill="none" stroke="#6b3a22" stroke-width="2" stroke-linejoin="round"/><circle cx="14" cy="22.5" r="1.6" fill="#6b3a22"/><circle cx="21" cy="22.5" r="1.6" fill="#6b3a22"/></svg>
    <div class="count">0</div>
  </div>
  <nav class="abs nav">
    <span class="active">HOME</span><span>ABOUT US</span><span>OUR PRODUCTS</span><span>CUSTOM SIGN</span><span>WOODWORKING</span><span>JEWELRY MANUFACTURER</span><span>CONTACT US</span>
  </nav>
  <div class="abs header-rule"></div>
</header>

<section class="abs hero" role="img" aria-label="Photo of a carved wooden farm sign on a routing machine">
  <h1>Quality Custom Signs &amp;<br>Woodcrafts</h1>
  <div class="btn-outline">GET STARTED
    <svg width="14" height="14" viewBox="0 0 14 14"><circle cx="7" cy="7" r="7" fill="#fff"/><path d="M5.5 4l3 3-3 3" fill="none" stroke="#6b4a30" stroke-width="1.8"/></svg>
  </div>
  <div class="dots"><i></i><i></i><i class="off"></i><i></i><i></i></div>
</section>

<h2 class="abs section-title" style="top:757px">Featured Products</h2>

<div class="abs card" style="left:111px;top:868px">
  <div class="photo" role="img" aria-label="Red custom farm sign" style="background:linear-gradient(#4e6a3c,#8a1f24 40%,#8a1f24 70%,#6a7a5a)"></div>
  <div class="name">CUSTOM SIGN</div><div class="stars">★★★★★</div><div class="price">$80.00</div>
</div>
<div class="abs card" style="left:359px;top:868px">
  <div class="photo" role="img" aria-label="Carved wooden panels" style="background:linear-gradient(90deg,#c9a97a,#e2c9a0 50%,#c59e6c)"></div>
  <div class="name">WOODWORKING</div><div class="stars">★★★★★</div><div class="price">$80.00</div>
</div>
<div class="abs card" style="left:607px;top:868px">
  <div class="photo" role="img" aria-label="Silver necklace on dark background" style="background:radial-gradient(circle at 55% 55%,#4a4a4a,#222)"></div>
  <div class="name">JEWELRY MANUFACTURER</div><div class="stars">★★★★★</div><div class="price">$80.00</div>
</div>
<div class="abs card" style="left:856px;top:868px">
  <div class="photo" role="img" aria-label="Small engraved wooden name plaque" style="background:linear-gradient(#e8e2d8,#d6cdbf 40%,#6b4a2e 45%,#6b4a2e 60%,#e6dfd4 65%)"></div>
  <div class="name">CUSTOM SIGN</div><div class="stars">★★★★★</div><div class="price">$80.00</div>
</div>

<section class="abs about" role="img" aria-label="Photo of a rustic barn event hall with long tables">
  <h2>About Us</h2>
  <p>Lorem ipsum dolor sit amet, consectetur adipiscing elit, sed do eiusmod tempor incididunt ut labore et dolore magna aliqua. Ut enim ad minim veniam, quis nostrud exercitation ullamco laboris nisi ut aliquip ex ea commodo consequat. Duis aute irure dolor in reprehenderit in voluptate velit esse cillum dolore eu fugiat nulla pariatur. Excepteur sint occaecat cupidatat non proident, sunt in culpa qui officia</p>
  <div class="btn-outline">GET STARTED
    <svg width="14" height="14" viewBox="0 0 14 14"><circle cx="7" cy="7" r="7" fill="#fff"/><path d="M5.5 4l3 3-3 3" fill="none" stroke="#444" stroke-width="1.8"/></svg>
  </div>
</section>

<h2 class="abs section-title" style="top:1808px">Best Seller</h2>

<div class="abs card" style="left:111px;top:1919px">
  <div class="photo" role="img" aria-label="Engraved wedding plaque" style="background:linear-gradient(#8a7a6a,#c9b08a 30%,#c9b08a 75%,#7a6a5c)"></div>
  <div class="name">PRODUCT TITLE</div><div class="stars">★★★★★</div><div class="price">$80.00</div>
</div>
<div class="abs card" style="left:359px;top:1919px">
  <div class="photo" role="img" aria-label="Carved wooden horse head" style="background:radial-gradient(circle at 55% 50%,#a06a42,#d8bc98 75%)"></div>
  <div class="name">PRODUCT TITLE</div><div class="stars">★★★★★</div><div class="price">$80.00</div>
</div>
<div class="abs card" style="left:607px;top:1919px">
  <div class="photo" role="img" aria-label="Wooden sign with anchor engraving" style="background:linear-gradient(90deg,#cdbb98,#e4d6b8 50%,#c9b690)"></div>
  <div class="name">PRODUCT TITLE</div><div class="stars">★★★★★</div><div class="price">$80.00</div>
</div>
<div class="abs card" style="left:856px;top:1919px">
  <div class="photo" role="img" aria-label="Silver necklace on dark background" style="background:radial-gradient(circle at 55% 55%,#4a4a4a,#222)"></div>
  <div class="name">PRODUCT TITLE</div><div class="stars">★★★★★</div><div class="price">$80.00</div>
</div>

<section class="abs testimonial">
  <h2>What Our Clients Says</h2>
  <div class="arrow" style="left:1010px"><svg width="34" height="33" viewBox="0 0 34 33"><path d="M19 10l-6 6.5 6 6.5" fill="none" stroke="#222" stroke-width="2"/></svg></div>
  <div class="arrow" style="left:1053px"><svg width="34" height="33" viewBox="0 0 34 33"><path d="M15 10l6 6.5-6 6.5" fill="none" stroke="#222" stroke-width="2"/></svg></div>
  <div class="avatar" role="img" aria-label="Client portrait"></div>
  <div class="vrule"></div>
  <svg class="abs" style="left:366px;top:154px" width="30" height="24" viewBox="0 0 30 24"><path d="M0 24V12C0 5 4 1 11 0v5c-3 1-5 3-5 6h5v13zM17 24V12c0-7 4-11 11-12v5c-3 1-5 3-5 6h5v13z" fill="#fff"/></svg>
  <p class="quote-text">Lorem ipsum dolor sit amet, consectetur adipiscing elit, sed do eiusmod tempor incididunt ut labore et dolore magna aliqua. Ut enim ad minim veniam, quis nostrud exercitation ullamco laboris nisi ut aliquip ex ea commodo consequat.</p>
  <div class="btn-outline">VIEW MORE
    <svg width="14" height="14" viewBox="0 0 14 14"><circle cx="7" cy="7" r="7" fill="#fff"/><path d="M5.5 4l3 3-3 3" fill="none" stroke="#7d4b2f" stroke-width="1.8"/></svg>
  </div>
  <div class="client">DANIEL HART</div>
</section>

<h2 class="abs section-title" style="top:2760px">Latest Blog</h2>

<article class="abs post" style="left:111px;top:2868px">
  <div class="photo" role="img" aria-label="Red farm sign outdoors in woods" style="background:linear-gradient(#7a6a58,#8a2a26 45%,#8a2a26 75%,#5a4a3a)"></div>
  <h3>LOREM IPSUM DOLOR SIT AMET, CONSE CTETUR ADIP</h3>
  <p>Sed ut perspiciatis unde omnis iste natus error sit voluptatem accusantdoloremque laudantium, totam rem aperiam</p>
  <div class="meta">
    <span><svg width="14" height="14" viewBox="0 0 14 14"><rect x="1" y="2" width="12" height="11" fill="none" stroke="#777" stroke-width="1.4"/><line x1="1" y1="5.5" x2="13" y2="5.5" stroke="#777" stroke-width="1.4"/></svg>Aug 27, 2020</span>
    <span><svg width="16" height="14" viewBox="0 0 16 14"><ellipse cx="7" cy="6" rx="6" ry="4.5" fill="none" stroke="#777" stroke-width="1.4"/></svg>( 0 ) Comments</span>
  </div>
</article>
<article class="abs post" style="left:446px;top:2868px">
  <div class="photo" role="img" aria-label="Man engraving a wooden board" style="background:linear-gradient(120deg,#2a2e3e,#3b4766 45%,#c9b08a 75%,#a08a6a)"></div>
  <h3>LOREM IPSUM DOLOR SIT AMET, CONSE CTETUR ADIP</h3>
  <p>Sed ut perspiciatis unde omnis iste natus error sit voluptatem accusantdoloremque laudantium, totam rem aperiam</p>
  <div class="meta">
    <span><svg width="14" height="14" viewBox="0 0 14 14"><rect x="1" y="2" width="12" height="11" fill="none" stroke="#777" stroke-width="1.4"/><line x1="1" y1="5.5" x2="13" y2="5.5" stroke="#777" stroke-width="1.4"/></svg>Jul 31, 2020</span>
    <span><svg width="16" height="14" viewBox="0 0 16 14"><ellipse cx="7" cy="6" rx="6" ry="4.5" fill="none" stroke="#777" stroke-width="1.4"/></svg>( 0 ) Comments</span>
  </div>
</article>
<article class="abs post" style="left:780px;top:2868px">
  <div class="photo" role="img" aria-label="Jeweler soldering at a workbench" style="background:linear-gradient(135deg,#6a5a4a,#a8907a 45%,#d8c8a8 70%,#5a4a3a)"></div>
  <h3>LOREM IPSUM DOLOR SIT AMET, CONSE CTETUR ADIP</h3>
  <p>Sed ut perspiciatis unde omnis iste natus error sit voluptatem accusantdoloremque laudantium, totam rem aperiam</p>
  <div class="meta">
    <span><svg width="14" height="14" viewBox="0 0 14 14"><rect x="1" y="2" width="12" height="11" fill="none" stroke="#777" stroke-width="1.4"/><line x1="1" y1="5.5" x2="13" y2="5.5" stroke="#777" stroke-width="1.4"/></svg>Jul 25, 2020</span>
    <span><svg width="16" height="14" viewBox="0 0 16 14"><ellipse cx="7" cy="6" rx="6" ry="4.5" fill="none" stroke="#777" stroke-width="1.4"/></svg>( 0 ) Comments</span>
  </div>
</article>

<footer class="abs footer">
  <div class="brand">Oakmere Creations, LLC</div>
  <div class="contact">
    <span><svg width="16" height="12" viewBox="0 0 16 12"><rect x="1" y="1" width="14" height="10" fill="none" stroke="#fff" stroke-width="1.3"/><path d="M1 1l7 6 7-6" fill="none" stroke="#fff" stroke-width="1.3"/></svg>info@oakmerecreations.com</span>
    <span class="sep">|</span>
    <span><svg width="14" height="14" viewBox="0 0 14 14"><path d="M3 1l2.5 3-1.5 2c1 2 2 3 4 4l2-1.5 3 2.5-1.5 2C6 12 2 8 1 2.5z" fill="#fff"/></svg>(555) 014-2273</span>
    <span class="sep">|</span>
    <span><svg width="12" height="16" viewBox="0 0 12 16"><path d="M6 15S1 9 1 6a5 5 0 0110 0c0 3-5 9-5 9z" fill="#fff"/><circle cx="6" cy="6" r="2" fill="#3b3b3b"/></svg>PO Box 18 Riverton, OH 45000</span>
  </div>
  <div class="frule"></div>
  <nav class="fnav"><span>HOME</span><span>ABOUT US</span><span>OUR PRODUCTS</span><span>CUSTOM SIGN</span><span>WOODWORKING</span><span>CONTACT US</span></nav>
</footer>
<div class="abs bottom-bar">
  <div class="copy">© 2020 Oakmere Creations. All Rights Reserved</div>
  <div class="pay"><i></i><i></i><i></i><i></i></div>
</div>

</body>
</html>
```